HOLTMARK Construction Services
Project: Stationary
Stationary
Simple
Derek Pannell
derek@hltservices-example.com
www.hltservices-example.com
Finalized Draft of the logo can be seen on the following URL: http://www.quillora-example.com/contests/business-logo-264. AI file will be uploaded soon. At the front of the business card the following text should be added design.engineer.build commercial.residential

```html
<!DOCTYPE html>
<html lang="en">
<head>
<meta charset="utf-8">
<title>HOLTMARK Construction Services – Stationery</title>
<link href="https://fonts.googleapis.com/css2?family=Questrial&display=swap" rel="stylesheet">
<style>
  :root {
    --green: #8cc63f;
    --black: #0b0b0b;
    --ink: #3a3a3a;
    --grey: #7a7a7a;
    --paper: #ffffff;
    --edge: #d6d6d6;
  }
  * { box-sizing: border-box; margin: 0; padding: 0; }
  html, body { width: 1200px; height: 749px; overflow: hidden; background: var(--paper); }
  body { position: relative; font-family: "Questrial", sans-serif; color: var(--ink); }

  .piece { position: absolute; overflow: hidden; border: 1px solid var(--edge); }
  .swoosh { position: absolute; left: 0; bottom: 0; width: 100%; display: block; }

  .brand { position: absolute; display: flex; flex-direction: column; align-items: center; color: var(--ink); line-height: 1; }
  .brand .dot { border-radius: 50%; background: var(--green); margin-bottom: 6px; }
  .brand .name { letter-spacing: 0.02em; }
  .brand .tag { letter-spacing: 0.2em; margin-top: 3px; }

  /* Letterhead */
  .letterhead { left: 24px; top: 29px; width: 523px; height: 691px; }
  .letterhead .brand { left: 26px; top: 38px; }
  .letterhead .dot { width: 62px; height: 62px; }
  .letterhead .name { font-size: 40px; }
  .letterhead .tag { font-size: 8.5px; }
  .letterhead .footer { position: absolute; left: 0; right: 0; bottom: 14px; text-align: center; font-size: 8px; color: var(--black); line-height: 1.7; }

  /* Business card front */
  .card-front { left: 571px; top: 29px; width: 228px; height: 134px; }
  .card-front .brand { left: 12px; top: 8px; }
  .card-front .dot { width: 24px; height: 24px; margin-bottom: 3px; }
  .card-front .name { font-size: 15px; }
  .card-front .tag { font-size: 3.6px; margin-top: 2px; }
  .card-front .person { position: absolute; left: 112px; top: 28px; font-size: 7px; line-height: 1.5; }
  .card-front .person .role { color: var(--green); font-size: 6px; }
  .card-front .contact { position: absolute; left: 0; right: 0; top: 72px; text-align: center; font-size: 5px; line-height: 1.8; }

  /* Card backs */
  .card-back { width: 221px; height: 126px; }
  .card-back .brand { left: 0; right: 0; top: 26px; }
  .card-back .dot { width: 30px; height: 30px; }
  .card-back .name { font-size: 22px; }
  .card-back .tag { font-size: 4.4px; }
  .card-green { left: 816px; top: 84px; background: var(--green); border-color: var(--green); }
  .card-green .brand { color: var(--paper); }
  .card-green .dot { background: var(--paper); }
  .card-black { left: 590px; top: 221px; background: var(--black); border-color: var(--black); }
  .card-black .brand { color: var(--paper); }
  .card-white { left: 902px; top: 233px; }
  .card-white .dot { background: var(--grey); }

  /* Envelope */
  .envelope { left: 569px; top: 379px; width: 593px; height: 341px; }
  .envelope .flap { position: absolute; left: 0; top: 0; width: 100%; display: block; }
  .envelope .brand { left: 14px; top: 100px; }
  .envelope .dot { width: 44px; height: 44px; }
  .envelope .name { font-size: 26px; }
  .envelope .tag { font-size: 5.2px; }
</style>
</head>
<body>

  <section class="piece letterhead" aria-label="Letterhead">
    <div class="brand">
      <span class="dot"></span>
      <span class="name">HOLTMARK</span>
      <span class="tag">CONSTRUCTION SERVICES</span>
    </div>
    <svg class="swoosh" viewBox="0 0 523 110" height="110" preserveAspectRatio="none" aria-hidden="true">
      <path d="M0 14 Q262 52 523 8 L523 20 Q262 64 0 26 Z" fill="var(--black)"/>
      <path d="M0 30 Q262 68 523 24 L523 110 L0 110 Z" fill="var(--green)"/>
    </svg>
    <p class="footer">commercial | HOME | residential<br>Phone: 555-010-4823 | Email: derek@hltservices-example.com | www.hltservices-example.com</p>
  </section>

  <section class="piece card-front" aria-label="Business card front">
    <div class="brand">
      <span class="dot"></span>
      <span class="name">HOLTMARK</span>
      <span class="tag">CONSTRUCTION SERVICES</span>
    </div>
    <p class="person">Derek Pannell<br><span class="role">design.engineer.build</span></p>
    <p class="contact">commercial.residential<br>P: 555-010-4823 | E: derek@hltservices-example.com | www.hltservices-example.com</p>
    <svg class="swoosh" viewBox="0 0 228 40" height="40" preserveAspectRatio="none" aria-hidden="true">
      <path d="M0 8 Q114 30 228 4 L228 10 Q114 38 0 14 Z" fill="var(--black)"/>
      <path d="M0 16 Q114 40 228 12 L228 40 L0 40 Z" fill="var(--green)"/>
    </svg>
  </section>

  <section class="piece card-back card-green" aria-label="Business card back, green">
    <div class="brand"><span class="dot"></span><span class="name">HOLTMARK</span><span class="tag">CONSTRUCTION SERVICES</span></div>
  </section>

  <section class="piece card-back card-black" aria-label="Business card back, black">
    <div class="brand"><span class="dot"></span><span class="name">HOLTMARK</span><span class="tag">CONSTRUCTION SERVICES</span></div>
  </section>

  <section class="piece card-back card-white" aria-label="Business card back, white">
    <div class="brand"><span class="dot"></span><span class="name">HOLTMARK</span><span class="tag">CONSTRUCTION SERVICES</span></div>
  </section>

  <section class="piece envelope" aria-label="Envelope">
    <svg class="flap" viewBox="0 0 593 90" height="90" preserveAspectRatio="none" aria-hidden="true">
      <path d="M0 0 H593 V82 Q296 70 0 82 Z" fill="var(--green)"/>
      <circle cx="296" cy="40" r="26" fill="var(--grey)"/>
    </svg>
    <div class="brand"><span class="dot"></span><span class="name">HOLTMARK</span><span class="tag">CONSTRUCTION SERVICES</span></div>
    <svg class="swoosh" viewBox="0 0 593 70" height="70" preserveAspectRatio="none" aria-hidden="true">
      <path d="M0 10 Q296 40 593 6 L593 16 Q296 52 0 20 Z" fill="var(--black)"/>
      <path d="M0 24 Q296 56 593 20 L593 70 L0 70 Z" fill="var(--green)"/>
    </svg>
  </section>

</body>
</html>
```